Tervoli Pizza & Pasta Takeaway Flyer

Our takeaway shop needs a well designed flyer for print and letter box distribution. Design to have a clear list of menu, Specials, contact details. If menu doesn't fit into A4, we won't mind going upto extended A4. I have attached draft copy of our menu and list of item in excel. Please add 5mm Bleed to the flyer.
Flyer will get printed on 115gsm Gloss stock.

Industry/Entity Type

Hospitality

```html
<!DOCTYPE html>
<html lang="en">
<head>
<meta charset="utf-8">
<title>Tervoli Pizza &amp; Pasta – Takeaway Menu</title>
<link rel="stylesheet" href="https://fonts.googleapis.com/css2?family=Roboto:wght@400;700&family=Roboto+Condensed:wght@400;700&family=Fredoka:wght@600&display=swap">
<style>
  :root{
    --bg:#ece7e1;
    --paper:#ffffff;
    --ink:#231a15;
    --heading:#3b2314;
    --red:#a3302b;
    --green:#6db33f;
    --dark:#2a2422;
    --photo-pizza-a:#b94a2c;
    --photo-pizza-b:#e7c49a;
    --photo-salad-a:#4f7d2a;
    --photo-salad-b:#c9b49a;
  }
  *{box-sizing:border-box;margin:0;padding:0}
  html,body{width:1200px;height:1200px;overflow:hidden;background:var(--bg)}
  .flyer{
    position:absolute;left:20px;top:293px;width:1350px;height:714px;
    transform:scale(0.8593);transform-origin:top left;
    background:var(--paper);color:var(--ink);
    font-family:"Roboto",Arial,sans-serif;overflow:hidden;
    box-shadow:0 2px 8px rgba(0,0,0,.18);
  }
  .panel{position:absolute;top:0}
  .col{position:absolute;top:6px;width:306px}
  .col--ribs{left:16px}
  .col--salad{left:353px}
  .sect{font-weight:700;font-size:14px;text-align:center;color:var(--heading);margin:2px 0 2px}
  .item{display:flex;align-items:baseline;font-size:12px;line-height:14.5px;white-space:nowrap}
  .item .dots{flex:1;border-bottom:1.5px dotted var(--ink);margin:0 2px;transform:translateY(-3px)}
  .item--lg{font-size:14px;line-height:17px;margin-top:2px}
  .desc{font-family:"Roboto Condensed",Arial,sans-serif;font-size:10.3px;line-height:14px;text-align:justify}
  .plain{font-size:12px;line-height:14.5px}
  .pack-title{display:flex;align-items:baseline;font-weight:700;font-size:17px;margin-top:6px}
  .pack-title .dots{flex:1;border-bottom:2px dotted var(--ink);margin:0 3px;transform:translateY(-4px)}
  .pack{text-align:center;font-size:13.5px;font-weight:700;line-height:17px;margin-top:2px}
  .pack small{font-family:"Roboto Condensed",Arial,sans-serif;font-weight:400;font-size:10.5px}
  .photo{position:absolute}
  .photo--salad{left:0;top:415px;width:337px;height:299px;
    background:radial-gradient(ellipse at 50% 60%,var(--photo-salad-a) 0 40%,#8a7158 62%,var(--photo-salad-b) 100%)}
  .photo--pizza{left:675px;top:0;width:675px;height:420px;
    background:radial-gradient(ellipse at 58% 48%,var(--photo-pizza-a) 0 38%,var(--photo-pizza-b) 55%,#7a4a33 80%,#5b3526 100%)}
  .curve{position:absolute}
  .green-panel{position:absolute;left:1013px;top:400px;width:337px;height:314px;background:var(--green)}
  .deals{position:absolute;left:690px;top:407px;width:305px}
  .deals h2{text-align:center;font-size:14px;color:var(--heading);font-weight:700}
  .deals .free{text-align:center;font-size:14px;margin:9px 0 6px}
  .deal{margin-top:4px}
  .deal .item{font-size:17px;line-height:20px;font-weight:700;color:var(--heading)}
  .deal .item .dots{border-bottom-width:2px}
  .deal .desc{font-size:10px;line-height:12px;margin-bottom:8px}
  .terms{font-size:11px;font-style:italic;line-height:15px;margin-top:2px}
  .brand{position:absolute;left:1065px;top:322px;width:232px;height:232px;border-radius:50%;
    background:var(--dark);border:8px solid #fff;display:flex;flex-direction:column;align-items:center;justify-content:center;color:#fff}
  .brand .name{font-size:44px;font-weight:700;line-height:1}
  .brand .sub{font-size:16px;font-weight:700;margin-top:8px}
  .ribbon{position:absolute;left:1025px;top:508px;width:310px;height:70px}
  .ribbon-text{position:absolute;left:1095px;top:505px;width:170px;text-align:center;
    font-family:"Fredoka",sans-serif;font-size:46px;color:#fff;line-height:66px}
  .contact{position:absolute;left:1013px;top:600px;width:337px;text-align:center;color:var(--ink)}
  .contact h3{font-size:11.5px;font-weight:700}
  .contact .big{font-size:22px;line-height:26px;margin-top:4px}
  .contact .addr{font-size:16px;line-height:20px}
</style>
</head>
<body>
<main class="flyer">

  <section class="panel">
    <div class="col col--ribs">
      <h2 class="sect">RIBS &amp; WINGS</h2>
      <div class="item">Pork Ribs<span class="dots"></span>$17</div>
      <div class="item">Beef Ribs<span class="dots"></span>$15</div>
      <div class="item">Buffalo Wings &nbsp;(6 Pcs)<span class="dots"></span>$8</div>
      <div class="item">BBQ Wings &nbsp;(6 Pcs)<span class="dots"></span>$8</div>
      <div class="item">Honey Soy wings &nbsp;(6 Pcs)<span class="dots"></span>$8</div>
      <div class="item">Fried Wings &nbsp;(6 Pcs)<span class="dots"></span>$8</div>
      <p class="plain">with Tomato Sauce</p>
      <div class="item">Chicken Lollipop &nbsp;(5 Pcs)<span class="dots"></span>$8</div>
      <p class="plain">With Lemon Wedges</p>
      <h2 class="sect">THE AB</h2>
      <div class="item">AB Chicken<span class="dots"></span>$13.95</div>
      <p class="desc">Marinated Chicken,Cheese on Top of Fries, Drizzled with Ranch, BBQ &amp; Garlic Sauce</p>
      <div class="item">AB Meat L<span class="dots"></span>$13.95</div>
      <p class="desc">Cheese, Pulled Beef, Bacon, Ham on Top of Fries, Drizzled with Ranch, BBQ &amp; Garlic Sauce</p>
      <div class="item">AB Combin<span class="dots"></span>$13.95</div>
      <p class="desc">Cheese, Chicken, Pulled Beef, Ham on Top of Fries, Drizzled with Ranch, BBQ &amp; Garlic Sauce</p>
      <div class="item">AB Veg<span class="dots"></span>$13.95</div>
      <p class="desc">Cheese, Tomato, Capsicum, Mushroom, crumbed Fetta, Pineappleon Top of Fries, Drizzled with Ranch, Tomato &amp; Garlic Sauce</p>
      <div class="item">AB Doubl<span class="dots"></span>$11.95</div>
      <p class="desc">Double Cheese on Top of Fries, Drizzled with Ranch, Tomato &amp; Garlic Sauce</p>
    </div>
    <div class="photo photo--salad" role="img" aria-label="Photo of a bowl of fresh kale salad with cranberries and seeds"></div>
    <svg class="curve" style="left:0;top:395px" width="337" height="50" viewBox="0 0 337 50">
      <path d="M0,12 C90,0 220,2 337,28 L337,0 L0,0 Z" fill="#fff"/>
      <path d="M0,30 C100,8 230,10 337,40 L337,26 C220,-2 90,-2 0,14 Z" fill="#fff"/>
      <path d="M0,18 C100,2 230,4 337,32" fill="none" stroke="var(--red)" stroke-width="9"/>
      <path d="M0,32 C100,16 230,18 337,44" fill="none" stroke="var(--red)" stroke-width="4"/>
    </svg>
  </section>

  <section class="panel">
    <div class="col col--salad">
      <h2 class="sect">SALAD</h2>
      <div class="item">Garden Salad<span class="dots"></span>$6</div>
      <p class="desc">Mixed Leaves, Tomato, Cucumber, Olives, Onion, Cucumber, Pineapple &amp; Italian dressing</p>
      <div class="item">Greek Salad<span class="dots"></span>$6</div>
      <p class="desc">Mixed Leaves, Tomato, Cucumber, Olives, Onion, Fetta &amp; Dressed with Lemon Juice, Olive Oil, White wine vinegar</p>
      <div class="item">Coleslaw<span class="dots"></span>$6</div>
      <p class="desc">Red Cabbages, Green Cabbage, Carrot, Onion mixed with Mayonnaise and Lemon</p>
      <div class="item">Chicken Ceaser Salad<span class="dots"></span>$9</div>
      <p class="desc">Mixed Leaves, Chicken, Crispy Bacon, Croutons, Parmesan Cheese &amp; Ceaser Dressing</p>
      <h2 class="sect">DESSERT</h2>
      <div class="item item--lg">Chocolate Sundae<span class="dots"></span>$4.95</div>
      <div class="item item--lg">Nocciola Calzone<span class="dots"></span>$6</div>
      <p class="desc">Calzone filled with Nocciola &amp; topped with Icing Sugar</p>
      <div class="item item--lg">Berry Zone<span class="dots"></span>$9</div>
      <p class="desc">Nocciola Calzone filled with Mixed Berry &amp; topped with Icing Sugar</p>
      <div class="item item--lg">White Valcone<span class="dots"></span>$9</div>
      <p class="desc">Calzone filled with White Chocolate &amp; topped with Icing Sugar</p>
      <div class="item item--lg">Crumbo Calzone<span class="dots"></span>$9</div>
      <p class="desc">Calzone rolled with Crumbo, filled with White Chocolate &amp; topped with Icing Sugar</p>
      <div class="item item--lg">Tropical Calzone<span class="dots"></span>$9</div>
      <p class="desc">Nocciola Calzone filled with Mango and Pineapple &amp; topped with Icing Sugar</p>
      <h2 class="sect">DRINKS</h2>
      <div class="item item--lg">Can<span class="dots"></span>$2.95</div>
      <p class="desc">Cola, Diet Cola, Cola Zero, Orange Fizz, Lemon Soda</p>
      <div class="item item--lg">1.25 lit<span class="dots"></span>$4.95</div>
      <p class="desc">Cola, Diet Cola, Cola Zero, Orange Fizz, Lemon Soda</p>
      <div class="item item--lg">Brookleaf Ice Tea<span class="dots"></span>$3.95</div>
      <div class="item item--lg">Orange Juice<span class="dots"></span>$4.50</div>
      <div class="item item--lg">Ginger Beer<span class="dots"></span>$3.95</div>
      <div class="item item--lg">Clearspring Water<span class="dots"></span>$2.50</div>
      <div class="item item--lg">Volt Energy Drink (375 ml)<span class="dots"></span>$3.95</div>
      <div class="pack-title">DINNER PACK<span class="dots"></span>$25</div>
      <p class="pack">Pizza Pack - <small>Cheesy Garlic Bread, Any Large Pizza<br>(Excl Premium range), Any Dessert or 1.25 lit</small></p>
      <p class="pack">Pasta Pack - <small>Curly Fries, Any Pasta, Any Dessert or 1.25 lit</small></p>
      <p class="pack">Parmi Pack - <small>Chips, Any Parmigiana, Any Dessert or 1.25 lit</small></p>
      <p class="pack">Ribs &amp; Wings Pack - <small>Chips, Any Wings, Ribs (Pork or Beef)</small></p>
    </div>
  </section>

  <div class="photo photo--pizza" role="img" aria-label="Photo of a margherita pizza topped with colourful cherry tomatoes and basil on a checked cloth"></div>
  <div class="green-panel"></div>
  <svg class="curve" style="left:675px;top:300px" width="675" height="140" viewBox="0 0 675 140">
    <path d="M0,140 L0,112 C120,42 300,18 420,28 C520,36 600,70 675,92 L675,140 Z" fill="#fff"/>
    <path d="M338,140 L338,22 C380,22 400,24 420,28 C520,36 600,70 675,92 L675,140 Z" fill="var(--green)"/>
    <path d="M0,118 C120,48 300,24 420,34 C520,42 600,76 675,98" fill="none" stroke="var(--green)" stroke-width="12"/>
    <path d="M70,96 C180,34 320,14 430,20 C530,26 610,56 675,74" fill="none" stroke="var(--red)" stroke-width="9"/>
  </svg>

  <section class="deals">
    <h2>DEALS</h2>
    <p class="free">Free delivery $40 and Over</p>
    <div class="deal"><div class="item">Party Deal<span class="dots"></span>$54.95</div>
      <p class="desc">3 Large Pizza or Pasta, 2 Garlic Bread &amp; 1.25 lit Drink</p></div>
    <div class="deal"><div class="item">Family Deal<span class="dots"></span>$39.95</div>
      <p class="desc">2 Large Pizza or Pasta, 2 Garlic Bread, 1.25 lit drink</p></div>
    <div class="deal"><div class="item">Couple Deal<span class="dots"></span>$24.95</div>
      <p class="desc">1 Family Pizza, 1 Garlic Bread, 1.25 lit Drink</p></div>
    <div class="deal"><div class="item">Single Deal<span class="dots"></span>$19.95</div>
      <p class="desc">1 Large Pizza or Pasta, 1 Garlic Bread, 1 can drink</p></div>
    <div class="deal"><div class="item">Small Deal<span class="dots"></span>$14.95</div>
      <p class="desc">1 Small Pizza, 1 Garlic Bread, 1 can drink - $14.95</p></div>
    <p class="terms">Terms &amp; Condition: (Large Pizza Excludes Premium &amp;<br>Seafood range,One &nbsp;Offer per order )</p>
  </section>

  <div class="brand">
    <span class="name">Tervoli</span>
    <span class="sub">Pizza &amp; Pasta</span>
  </div>

  <svg class="ribbon" width="310" height="70" viewBox="0 0 310 70">
    <path d="M0,20 L80,20 L80,62 L0,62 L22,41 Z" fill="var(--red)"/>
    <path d="M310,20 L230,20 L230,62 L310,62 L288,41 Z" fill="var(--red)"/>
    <path d="M62,62 L80,70 L80,62 Z" fill="#6b1d1a"/>
    <path d="M248,62 L230,70 L230,62 Z" fill="#6b1d1a"/>
    <rect x="66" y="4" width="178" height="58" fill="var(--red)" stroke="#fff" stroke-width="2"/>
  </svg>
  <div class="ribbon-text">MENU</div>

  <section class="contact">
    <h3>Contact Details</h3>
    <p class="big">CONTACT US : 07 3555 0199</p>
    <p class="addr">Tervoli Pizza &amp; Pasta</p>
    <p class="addr">118 Harbour View Rd, Westbrook</p>
    <p class="big" style="margin-top:2px">LOG ON : www.tervoli.com.au</p>
  </section>

</main>
</body>
</html>
```